Mental health agency needs an ad for brochure

Please provide us with a half page (W 8.5 inches x H 5.5 inches) advertising our company. We are a mental health agency that provides training, education, and consultation for companies that serve children, adolescents, or adults. We can offer training and education to help companies better serve their clientele and consultation about how companies are currently working with their staff or clientele. Our website is www.bridgelumen.com and they can contact us at info@kestrelhollowinstitute.com or 503-274-8816.

```html
<!DOCTYPE html>
<html lang="en">
<head>
<meta charset="utf-8">
<title>Kestrel Hollow Institute – Half Page Ad</title>
<link rel="stylesheet" href="https://fonts.googleapis.com/css2?family=Noto+Serif:wght@400;600;700&display=swap">
<style>
  :root {
    --navy: #06306e;
    --teal: #00a0c6;
    --teal-light: #0b9cc4;
    --slate: #737373;
    --ink: #2a2a2a;
    --paper: #ffffff;
    --backdrop: #e4e4e4;
    --photo-green: #6f9a4c;
    --photo-warm: #c9a98a;
  }
  * { box-sizing: border-box; margin: 0; padding: 0; }
  html, body {
    width: 1200px; height: 1031px; overflow: hidden;
    background: var(--backdrop);
    font-family: "Noto Serif", Georgia, serif;
  }
  .ad {
    position: absolute; left: 0; top: 128px;
    width: 1200px; height: 775px;
    background: var(--paper);
    overflow: hidden;
  }
  .hero { position: absolute; left: 0; top: 0; width: 1200px; height: 400px; }
  .hero-art { position: absolute; inset: 0; }
  .brand {
    position: absolute; left: 58px; top: 42px;
    display: flex; align-items: center; gap: 18px;
  }
  .brand-mark {
    width: 86px; height: 86px; border-radius: 50%;
    background: var(--navy);
  }
  .brand-name {
    font-size: 31px; font-weight: 600; color: var(--navy);
    letter-spacing: 0.5px;
  }
  .intro { position: absolute; left: 52px; top: 176px; width: 575px; list-style: none; }
  .intro li {
    position: relative; padding-left: 31px;
    font-size: 19.5px; line-height: 27px; color: var(--ink);
    margin-bottom: 16px;
  }
  .intro li::before {
    content: ""; position: absolute; left: 0; top: 6px;
    width: 15px; height: 15px; border-radius: 50%;
    background: var(--navy);
  }
  .tagline {
    position: absolute; left: 0; top: 400px; width: 1200px; height: 67px;
    background: linear-gradient(90deg, var(--teal-light) 0%, var(--navy) 100%);
    color: var(--paper); font-weight: 700; font-size: 39px;
    display: flex; align-items: center; justify-content: center;
    letter-spacing: 0.3px;
  }
  .services {
    position: absolute; left: 0; top: 467px; width: 1200px; height: 244px;
    display: grid; grid-template-columns: repeat(3, 400px);
  }
  .service {
    color: var(--paper); text-align: center;
    font-size: 18.5px; line-height: 24px;
    padding: 66px 40px 0;
  }
  .service--navy { background: var(--navy); }
  .service--teal { background: var(--teal); color: #e8f8fc; padding-top: 16px; }
  .service--slate { background: var(--slate); }
  .service-heading {
    display: flex; align-items: center; justify-content: center; gap: 8px;
    color: var(--paper); font-size: 28px; font-weight: 700; line-height: 34px;
    white-space: nowrap;
    margin: 0 -30px 18px;
  }
  .service-heading::before, .service-heading::after {
    content: ""; width: 30px; height: 2px; background: var(--paper); flex: none;
  }
  .contact {
    position: absolute; left: 0; top: 711px; width: 1200px; height: 64px;
    display: flex; align-items: center; justify-content: center; gap: 16px;
    color: var(--navy); font-size: 24px;
  }
  .contact-item { display: flex; align-items: center; gap: 9px; }
  .contact-item svg { width: 24px; height: 24px; }
  .contact-phone { font-weight: 700; }
  .contact-accent { color: var(--teal); font-weight: 700; }
  .contact-divider { width: 2px; height: 24px; background: var(--teal); }
</style>
</head>
<body>
<main class="ad">
  <section class="hero">
    <svg class="hero-art" viewBox="0 0 1200 400" width="1200" height="400">
      <defs>
        <linearGradient id="photoTone" x1="0" y1="0" x2="1" y2="1">
          <stop offset="0" stop-color="#6f9a4c"/>
          <stop offset="0.6" stop-color="#c9a98a"/>
          <stop offset="1" stop-color="#4f7fb8"/>
        </linearGradient>
      </defs>
      <polygon points="778,0 1200,0 1200,400 588,400" fill="url(#photoTone)" role="img" aria-label="Photo of a smiling family of five standing outdoors among green trees"/>
      <line x1="776" y1="0" x2="700" y2="138" stroke="#00a0c6" stroke-width="4"/>
      <polygon points="702,138 724,138 588,400 552,400" fill="#06306e"/>
    </svg>
    <div class="brand">
      <span class="brand-mark"></span>
      <span class="brand-name">Kestrel Hollow Institute</span>
    </div>
    <ul class="intro">
      <li>We are a mental health agency that provides training, education, and consultation for companies that serve children, adolescents, or adults.</li>
      <li>We can offer training and education to help companies better serve their clientele and consultation about how companies are currently working with their staff or clientele.</li>
    </ul>
  </section>

  <h1 class="tagline">Nurture Authentic and Safe Relationships Around You</h1>

  <section class="services">
    <p class="service service--navy">Reduce stress and develop poise in managing behaviors in your school and non-profit child-serving organizations with training in the area of trauma and its effect on the brain and body.</p>
    <div class="service service--teal">
      <h2 class="service-heading">WHAT WE PROVIDE</h2>
      <p>Develop confidence and become self-assured to build strong and reliable boundaries in relationship with others using body-oriented therapy, offered<br>for individuals, couples, and families.</p>
    </div>
    <p class="service service--slate">Decrease staff stress, burnout, and absenteeism while increasing staff authenticity and openness using feedback and heatmapping tools across teams and departments in your organization.</p>
  </section>

  <footer class="contact">
    <span class="contact-item contact-phone">
      <svg viewBox="0 0 24 24"><circle cx="12" cy="12" r="12" fill="#00a0c6"/><path d="M8 6.5l2 0 1 3-1.5 1a7 7 0 0 0 4 4l1-1.5 3 1v2a1.5 1.5 0 0 1-1.5 1.5A10 10 0 0 1 6.5 8 1.5 1.5 0 0 1 8 6.5z" fill="#fff"/></svg>
      503-274-8816
    </span>
    <span class="contact-divider"></span>
    <span class="contact-item">
      <svg viewBox="0 0 24 24"><circle cx="12" cy="12" r="12" fill="#00a0c6"/><rect x="6" y="8" width="12" height="8" rx="1" fill="#fff"/><path d="M6.5 8.5l5.5 4 5.5-4" stroke="#00a0c6" stroke-width="1.3" fill="none"/></svg>
      <span>info@<span class="contact-accent">kestrelhollowinstitute</span>.com</span>
    </span>
    <span class="contact-divider"></span>
    <span class="contact-item">
      <svg viewBox="0 0 24 24"><circle cx="12" cy="12" r="12" fill="#00a0c6"/><g stroke="#fff" stroke-width="1.2" fill="none"><circle cx="12" cy="12" r="6.5"/><ellipse cx="12" cy="12" rx="3" ry="6.5"/><line x1="5.5" y1="12" x2="18.5" y2="12"/><line x1="6.5" y1="9" x2="17.5" y2="9"/><line x1="6.5" y1="15" x2="17.5" y2="15"/></g></svg>
      <span>www.<span class="contact-accent">bridgelumen</span>.com</span>
    </span>
  </footer>
</main>
</body>
</html>
```